Velvet Jubilee Flyer

I need an 8.5x11 or 8.5x14 or 11x17 flyer for a benefit concert. Logo has already been designed; uploading several different versions, and you could choose which you want to use. For flyer design: something subtly musical (not a big fan of using musical symbols in the design, treble clefs, eighth notes, etc.) But something classy. I'm uploading unformatted copy, and two logos: one of the radio station that is helping to sponsor the event, and one for the organization the concert is benefitting. This is quick turnaround, so I promise to be very responsive with feedback. Thanks!

```html
<!DOCTYPE html>
<html lang="en">
<head>
<meta charset="utf-8">
<title>Midwinter Velvet Jubilee – Flyer</title>
<link rel="stylesheet" href="https://fonts.googleapis.com/css2?family=Montserrat:wght@700&family=Roboto+Condensed:wght@300;400;700&display=swap">
<style>
  :root {
    --page-bg: #e6e4e1;
    --ink-dark: #323b47;
    --lime: #d6df2b;
    --white: #ffffff;
    --teal: #2f7fa3;
    --blue-deep: #2d5f8e;
    --pink: #f2a3a8;
    --mint: #bfe6b0;
    --cream: #fdf3e6;
  }
  * { margin: 0; padding: 0; box-sizing: border-box; }
  html, body {
    width: 1200px; height: 692px; overflow: hidden;
    background: var(--page-bg);
  }
  .flyer {
    position: absolute; left: 376px; top: 0;
    width: 448px; height: 692px; overflow: hidden;
    font-family: "Roboto Condensed", "Arial Narrow", sans-serif;
  }
  .backdrop {
    position: absolute; inset: 0;
    background:
      radial-gradient(ellipse 60% 40% at 95% 18%, var(--pink) 0%, rgba(242,163,168,0) 70%),
      radial-gradient(ellipse 55% 35% at 85% 85%, var(--mint) 0%, rgba(191,230,176,0) 75%),
      radial-gradient(ellipse 45% 40% at 75% 55%, var(--cream) 0%, rgba(253,243,230,0) 70%),
      linear-gradient(160deg, var(--teal) 0%, var(--blue-deep) 45%, #4a8fae 70%, #9fd6c0 100%);
  }
  .shape { position: absolute; inset: 0; }
  .title {
    position: absolute; left: 40px; top: 92px; width: 290px;
    font-family: "Montserrat", sans-serif; font-weight: 700;
    color: var(--ink-dark); text-transform: uppercase; line-height: 1.02;
  }
  .title .line-small { display: block; font-size: 27px; letter-spacing: 1px; }
  .title .line-big { display: block; font-size: 40px; letter-spacing: -0.5px; }
  .details { position: absolute; left: 22px; top: 282px; }
  .details p { text-transform: uppercase; line-height: 1; }
  .accent { color: var(--lime); font-weight: 300; }
  .strong { color: var(--white); font-weight: 700; }
  .live { font-size: 48px; }
  .artist { font-size: 42px; margin-top: 2px; }
  .day { font-size: 34px; margin-top: 22px; }
  .date { font-size: 31px; margin-top: 2px; }
  .at { font-size: 28px; margin-top: 24px; }
  .venue { font-size: 30px; margin-top: 0; }
  .time { font-size: 26px; margin-top: 20px; color: var(--lime); font-weight: 700; }
  .sponsors { position: absolute; left: 20px; top: 614px; width: 200px; text-align: center; }
  .sponsors-label { font-size: 13px; color: var(--ink-dark); letter-spacing: 0.5px; text-transform: uppercase; }
  .sponsor-list { display: flex; justify-content: space-between; align-items: center; margin-top: 12px; }
  .sponsor-name {
    display: flex; align-items: center; gap: 4px;
    font-size: 11px; font-weight: 700; color: var(--ink-dark); text-transform: uppercase; line-height: 1.05;
  }
  .sponsor-name .mark { width: 9px; height: 9px; background: var(--ink-dark); flex: none; }
</style>
</head>
<body>
  <main class="flyer">
    <div class="backdrop" role="img" aria-label="Soft painted winter backdrop in teal, pink and mint with a line drawing of an electric guitar"></div>

    <svg class="shape" width="448" height="692" viewBox="0 0 448 692" aria-hidden="true">
      <path fill="#ffffff" d="M0,0 H448 V70 C420,88 368,58 358,92 C350,122 448,118 448,160 C448,202 372,172 352,212 C336,248 326,270 258,263 C180,255 82,272 30,250 C6,238 0,220 0,200 Z"/>
      <path fill="#ffffff" d="M0,600 C80,594 180,602 232,640 C262,664 296,692 322,692 H0 Z"/>
    </svg>

    <h1 class="title">
      <span class="line-small">Midwinter</span>
      <span class="line-big">Velvet Jubilee</span>
    </h1>

    <section class="details">
      <p class="accent live">Live Music</p>
      <p class="strong artist">Artist Name</p>
      <p class="accent day">Saturday</p>
      <p class="strong date">January 6</p>
      <p class="accent at">At</p>
      <p class="strong venue">Music Hall</p>
      <p class="time">Starts at 8PM</p>
    </section>

    <footer class="sponsors">
      <p class="sponsors-label">Sponsored by</p>
      <div class="sponsor-list">
        <span class="sponsor-name"><span class="mark"></span>Riverbend<br>Shelter Care</span>
        <span class="sponsor-name">KVLS 91.3</span>
      </div>
    </footer>
  </main>
</body>
</html>
```